The next stage in our 106 year history in Specialised Stationery

We need a business card design(which is also adaptable for our general stationery) to suit the changing face of our business. Brevik, an Australian company has been the leader in its category since 1907. We design and print various books required by small business to comply with government legislation in regards to keeping records. Accountancy, Payroll, Vehicle usage recording, Firearms registration etc. The Brevik logo a blue diamond is one of the best known in our industry. As manual recording has declined in the last few years we have diversified into other areas: Safety Apparel, Personal Protective Equipment (PPE) and web based software for bookkeeping and Customer Relationship management(CRM). Separate logos have been adopted for each of these being: Brevik Systems, Brevik Safety, Brevik Apparel and Brevik Software each with same diamond but different colour background. This has made it easy to identify the different sectors but difficult to bring together for a Corporate identity in Business cards etc. We are looking to bring all logos together (not one logo) but still allow the logo to depict the diversity of our offering, while still being able to have a category specific logo for each of the divisions. All products go through the same distribution channel, Office Products. The final design should depict an old established company well, known and trusted but leaping forward and still retaining same values they have come to trust.

Target Market(s)

Micro to small business companies generally who employ 20 or less people.

Industry/Entity Type

Small Business

Requirements
Must have
• The diamonds are well recognised and the new design should retain the integrity of them.

```html
<!DOCTYPE html>
<html lang="en">
<head>
<meta charset="utf-8">
<title>Brevik Business Card</title>
<link rel="stylesheet" href="https://fonts.googleapis.com/css2?family=Arimo:wght@700&family=Open+Sans:wght@600;700&display=swap">
<style>
  :root {
    --backdrop: #d6d6d6;
    --card-white: #ffffff;
    --sky-blue: #0a8ff0;
    --brand-blue: #1a5faa;
    --brand-red: #c0002e;
    --brand-orange: #e8592a;
    --brand-green: #23b33a;
    --navy: #1b3580;
    --divider: #8a8a8a;
  }
  * { margin: 0; padding: 0; box-sizing: border-box; }
  html, body { width: 1200px; height: 800px; overflow: hidden; }
  body {
    background: var(--backdrop);
    position: relative;
    font-family: "Open Sans", Arial, sans-serif;
  }
  .card {
    position: absolute;
    top: 242px;
    width: 550px;
    height: 316px;
    background: var(--card-white);
    overflow: hidden;
    box-shadow: 0 6px 18px rgba(0,0,0,0.25);
  }
  /* Front */
  .card-front { left: 33px; }
  .quadrant { position: absolute; width: 50%; height: 50%; }
  .quadrant-systems { left: 0; top: 0; background: var(--sky-blue); }
  .quadrant-software { right: 0; top: 0; background: var(--brand-red); }
  .quadrant-safety { left: 0; bottom: 0; background: var(--brand-orange); }
  .quadrant-apparel { right: 0; bottom: 0; background: var(--brand-green); }
  .front-wordmark {
    position: absolute;
    inset: 0;
    display: flex;
    align-items: center;
    justify-content: center;
    font-family: "Arimo", Arial, sans-serif;
    font-weight: 700;
    font-size: 72px;
    letter-spacing: 1px;
    color: var(--card-white);
  }
  /* Back */
  .card-back { left: 617px; }
  .band { position: absolute; height: 20px; }
  .band-top-blue { top: 0; left: 0; width: 330px; background: var(--brand-blue); }
  .band-top-red { top: 0; left: 330px; right: 0; background: var(--brand-red); }
  .band-bottom-orange { bottom: 0; left: 0; width: 260px; height: 22px; background: var(--brand-orange); }
  .band-bottom-green { bottom: 0; left: 260px; right: 0; height: 22px; background: var(--brand-green); }

  .divisions {
    position: absolute;
    left: 40px;
    top: 52px;
    width: 200px;
    list-style: none;
    display: grid;
    grid-template-columns: 1fr 1fr;
    gap: 16px 14px;
  }
  .division {
    display: flex;
    align-items: center;
    gap: 8px;
    font-family: "Arimo", Arial, sans-serif;
    font-weight: 700;
    font-size: 12px;
    line-height: 1.2;
    color: var(--navy);
    text-transform: uppercase;
  }
  .division-label { display: block; }
  .division-square { width: 14px; height: 14px; flex: none; }
  .division-systems .division-square { background: var(--brand-blue); }
  .division-safety .division-square { background: var(--brand-orange); }
  .division-software .division-square { background: var(--brand-red); }
  .division-apparel .division-square { background: var(--brand-green); }

  .company-name {
    position: absolute;
    left: 34px;
    top: 180px;
    font-family: "Arimo", Arial, sans-serif;
    font-weight: 700;
    font-size: 24px;
    color: var(--navy);
  }
  .company-address {
    position: absolute;
    left: 34px;
    top: 214px;
    font-style: normal;
    font-weight: 700;
    font-size: 11.5px;
    line-height: 1.45;
    color: var(--brand-red);
  }
  .card-divider {
    position: absolute;
    left: 268px;
    top: 42px;
    width: 1.5px;
    height: 224px;
    background: var(--divider);
  }
  .person-name {
    position: absolute;
    left: 300px;
    top: 54px;
    font-family: "Arimo", Arial, sans-serif;
    font-weight: 700;
    font-size: 24px;
    color: var(--brand-blue);
  }
  .person-title {
    position: absolute;
    left: 300px;
    top: 86px;
    font-family: "Arimo", Arial, sans-serif;
    font-weight: 700;
    font-size: 16px;
    color: var(--brand-red);
  }
  .contact-list {
    position: absolute;
    left: 290px;
    top: 178px;
    list-style: none;
  }
  .contact-item {
    display: flex;
    align-items: center;
    gap: 8px;
    height: 22px;
    font-weight: 600;
    font-size: 12.5px;
    color: var(--brand-red);
  }
  .contact-icon { width: 14px; height: 14px; fill: var(--brand-blue); flex: none; }
</style>
</head>
<body>

<section class="card card-front" aria-label="Card front">
  <div class="quadrant quadrant-systems"></div>
  <div class="quadrant quadrant-software"></div>
  <div class="quadrant quadrant-safety"></div>
  <div class="quadrant quadrant-apparel"></div>
  <div class="front-wordmark">Brevik</div>
</section>

<section class="card card-back" aria-label="Card back">
  <div class="band band-top-blue"></div>
  <div class="band band-top-red"></div>

  <ul class="divisions">
    <li class="division division-systems"><span class="division-square"></span><span><span class="division-label">Brevik</span><span class="division-label">Systems</span></span></li>
    <li class="division division-software"><span class="division-square"></span><span><span class="division-label">Brevik</span><span class="division-label">Software</span></span></li>
    <li class="division division-safety"><span class="division-square"></span><span><span class="division-label">Brevik</span><span class="division-label">Safety</span></span></li>
    <li class="division division-apparel"><span class="division-square"></span><span><span class="division-label">Brevik</span><span class="division-label">Apparel</span></span></li>
  </ul>

  <h1 class="company-name">Brevik Pty Limited</h1>
  <address class="company-address">Unit 4, 218 Harbour Street,<br>Kelso, NSW 2795</address>

  <div class="card-divider"></div>

  <h2 class="person-name">YOUR NAME</h2>
  <p class="person-title">Title</p>

  <ul class="contact-list">
    <li class="contact-item">
      <svg class="contact-icon" viewBox="0 0 24 24" aria-hidden="true"><path d="M6.6 10.8a15.1 15.1 0 0 0 6.6 6.6l2.2-2.2a1 1 0 0 1 1-.25 11.4 11.4 0 0 0 3.6.57 1 1 0 0 1 1 1V20a1 1 0 0 1-1 1A17 17 0 0 1 3 4a1 1 0 0 1 1-1h3.5a1 1 0 0 1 1 1c0 1.250.2 2.450.57 3.6a1 1 0 0 1-.25 1z"/></svg>
      61 2 5550 1234
    </li>
    <li class="contact-item">
      <svg class="contact-icon" viewBox="0 0 24 24" aria-hidden="true"><path d="M6 2h12v5H6zM3 8h18a2 2 0 0 1 2 2v7h-4v5H5v-5H1v-7a2 2 0 0 1 2-2zm4 8v4h10v-4z"/></svg>
      61 2 5550 5678
    </li>
    <li class="contact-item">
      <svg class="contact-icon" viewBox="0 0 24 24" aria-hidden="true"><path d="M2 5h20v14H2zm2 2v.5l8 5 8-5V7zm0 2.8V17h16V9.8l-8 5z"/></svg>
      hello@brevikmail.com
    </li>
    <li class="contact-item">
      <svg class="contact-icon" viewBox="0 0 24 24" aria-hidden="true"><path d="M12 2a10 10 0 1 0 0 20 10 10 0 0 0 0-20zm6.9 6h-2.9a15.6 15.6 0 0 0-1.4-3.6A8 8 0 0 1 18.9 8zM12 4c.8 1.2 1.5 2.5 1.9 4h-3.8c.4-1.5 1.1-2.8 1.9-4zM4.3 14a8 8 0 0 1 0-4h3.4a16 16 0 0 0 0 4zm.8 2h2.9c.3 1.3.8 2.5 1.4 3.6A8 8 0 0 1 5.1 16zM8 8H5.1a8 8 0 0 1 4.3-3.6C8.8 5.5 8.3 6.7 8 8zm4 12c-.8-1.2-1.5-2.5-1.9-4h3.8c-.4 1.5-1.1 2.8-1.9 4zm2.3-6H9.7a14 14 0 0 1 0-4h4.6a14 14 0 0 1 0 4zm.3 5.6c.6-1.1 1.1-2.3 1.4-3.6h2.9a8 8 0 0 1-4.3 3.6zM16.3 14a16 16 0 0 0 0-4h3.4a8 8 0 0 1 0 4z"/></svg>
      www.brevik-office.com.au
    </li>
  </ul>

  <div class="band band-bottom-orange"></div>
  <div class="band band-bottom-green"></div>
</section>

</body>
</html>
```